Create an Engaging Yet Simple Cycle Infographic to be featured in new book

I require a clearly designed, simple to navigate infographic. It will depict a "CYCLE-style" Framework that includes 7-stages which are underpinned by 6-enablers. The cycle is the core concept of a new business book. Each component also needs a simple graphic/ icon that can be used as a short-cut to identify the specific stage or enabler. The attached brief provides further details.

Target Market(s)

Business leaders

Font styles to use
Serif

Colors
000000

Requirements
Must have
• Simple, easy to engage with, fit on portrait-oriented book page

```html
<!DOCTYPE html>
<html lang="en">
<head>
<meta charset="utf-8">
<title>The Cycle Framework</title>
<link rel="stylesheet" href="https://fonts.googleapis.com/css2?family=Montserrat:wght@500;600;800&display=swap">
<style>
  :root {
    --header-bg: #363636;
    --header-text: #ffffff;
    --page-bg: #ffffff;
    --green-dark: #17592a;
    --green-bright: #2fa04a;
    --dome-green: #4e7b57;
    --ring-grey: #c9c7cc;
    --panel-grey: #c6c5c9;
    --tile-green: #cfe3c9;
    --icon-ink: #2c2c2c;
    --label-ink: #2a2a2a;
    --stage-border: #2e9245;
  }
  * { margin: 0; padding: 0; box-sizing: border-box; }
  html, body { width: 788px; height: 1200px; overflow: hidden; background: var(--page-bg); }
  .canvas { position: relative; width: 788px; height: 1200px; font-family: "Montserrat", Arial, sans-serif; }
  .title-band {
    position: absolute; left: 0; top: 0; width: 788px; height: 136px;
    background: var(--header-bg);
    display: flex; align-items: center; justify-content: center;
  }
  .title-band h1 {
    color: var(--header-text); font-weight: 800; font-size: 46px; letter-spacing: 1px;
  }
  .diagram { position: absolute; left: 0; top: 0; }
  .stage-label {
    position: absolute; transform: translateX(-50%);
    font-size: 17px; font-weight: 600; color: var(--label-ink); letter-spacing: 0.3px; white-space: nowrap;
  }
  .enablers {
    position: absolute; left: 40px; top: 862px; width: 708px; height: 176px;
    background: var(--panel-grey);
    display: flex; gap: 12px; padding: 12px;
  }
  .enabler { flex: 1; display: flex; flex-direction: column; gap: 6px; }
  .enabler-icon {
    height: 86px; background: var(--tile-green);
    display: flex; align-items: center; justify-content: center;
  }
  .enabler-name {
    flex: 1; background: #ffffff;
    display: flex; align-items: center; justify-content: center; text-align: center;
    font-size: 13px; font-weight: 500; line-height: 1.3; color: var(--label-ink);
  }
</style>
</head>
<body>
<div class="canvas">
  <header class="title-band"><h1>THE CYCLE FRAMEWORK</h1></header>

  <svg class="diagram" width="788" height="1200" viewBox="0 0 788 1200">
    <defs>
      <linearGradient id="arch-green" x1="0" y1="0" x2="1" y2="0">
        <stop offset="0" stop-color="var(--green-dark)"/>
        <stop offset="0.5" stop-color="var(--green-bright)"/>
        <stop offset="1" stop-color="var(--green-dark)"/>
      </linearGradient>
    </defs>

    <!-- central upward arrow -->
    <polygon points="394,628 584,786 482,786 482,862 306,862 306,786 204,786" fill="var(--ring-grey)"/>

    <!-- green outer arch -->
    <path d="M 64 780 A 330 360 0 0 1 724 780 L 684 780 A 290 320 0 0 0 104 780 Z" fill="url(#arch-green)"/>

    <!-- grey flow ring -->
    <path d="M 114 780 A 280 310 0 0 1 674 780 L 644 780 A 250 280 0 0 0 144 780 Z" fill="var(--ring-grey)"/>

    <!-- inner dome -->
    <path d="M 144 780 A 250 280 0 0 1 644 780 Z" fill="var(--dome-green)"/>
    <polygon points="394,640 560,780 228,780" fill="var(--ring-grey)"/>

    <!-- flow arrowheads on the ring -->
    <g fill="#ffffff" opacity="0.85">
      <polygon points="-12,-14 14,0 -12,14" transform="translate(221,566) rotate(-48)"/>
      <polygon points="-12,-14 14,0 -12,14" transform="translate(394,485)"/>
      <polygon points="-12,-14 14,0 -12,14" transform="translate(567,566) rotate(48)"/>
      <polygon points="-12,-14 14,0 -12,14" transform="translate(651,740) rotate(82)"/>
    </g>

    <!-- stage markers -->
    <g class="stage-marks" fill="#ffffff" stroke="var(--stage-border)" stroke-width="3">
      <rect x="55" y="751" width="58" height="58"/>
      <rect x="68" y="539" width="58" height="58"/>
      <rect x="201" y="398" width="58" height="58"/>
      <rect x="365" y="351" width="58" height="58"/>
      <rect x="529" y="398" width="58" height="58"/>
      <rect x="662" y="539" width="58" height="58"/>
      <rect x="675" y="751" width="58" height="58"/>
    </g>

    <g fill="var(--icon-ink)" stroke="var(--icon-ink)">
      <!-- see: bulb -->
      <g transform="translate(84,780)">
        <circle cx="0" cy="-5" r="11" fill="none" stroke-width="3"/>
        <rect x="-5" y="7" width="10" height="8" stroke="none"/>
        <g stroke-width="2.5"><line x1="0" y1="-24" x2="0" y2="-19"/><line x1="-18" y1="-12" x2="-14" y2="-9"/><line x1="18" y1="-12" x2="14" y2="-9"/></g>
      </g>
      <!-- understand: gauge -->
      <g transform="translate(97,570)" stroke="none">
        <path d="M -18 8 A 18 18 0 0 1 18 8 Z"/>
        <rect x="-20" y="10" width="40" height="4"/>
      </g>
      <!-- prioritise: bars -->
      <g transform="translate(230,427)" stroke="none">
        <rect x="-16" y="-15" width="32" height="30" rx="4"/>
        <g fill="#ffffff"><rect x="-10" y="-9" width="20" height="4"/><rect x="-10" y="-2" width="14" height="4"/><rect x="-10" y="5" width="8" height="4"/></g>
      </g>
      <!-- design: stacked layers -->
      <g transform="translate(394,380)" stroke="none">
        <rect x="-10" y="-16" width="26" height="20"/>
        <rect x="-14" y="-10" width="26" height="20" fill="#ffffff" stroke="var(--icon-ink)" stroke-width="2"/>
        <rect x="-18" y="-4" width="26" height="20"/>
      </g>
      <!-- plan: clipboard -->
      <g transform="translate(558,427)">
        <rect x="-13" y="-16" width="26" height="32" fill="none" stroke-width="3"/>
        <g stroke-width="2"><line x1="-7" y1="-7" x2="7" y2="-7"/><line x1="-7" y1="0" x2="7" y2="0"/><line x1="-7" y1="7" x2="7" y2="7"/></g>
      </g>
      <!-- move: rising chart -->
      <g transform="translate(691,570)" stroke="none">
        <rect x="-16" y="4" width="6" height="12"/><rect x="-7" y="-2" width="6" height="18"/><rect x="2" y="-8" width="6" height="24"/><rect x="11" y="-14" width="6" height="30"/>
        <polyline points="-16,-2 -4,-10 4,-6 16,-20" fill="none" stroke="var(--icon-ink)" stroke-width="2"/>
      </g>
      <!-- learn: head badge -->
      <g transform="translate(704,780)">
        <circle cx="0" cy="-2" r="14" stroke="none"/>
        <circle cx="0" cy="-2" r="5" fill="#ffffff" stroke="none"/>
        <rect x="-5" y="11" width="10" height="7" stroke="none"/>
      </g>
    </g>
  </svg>

  <span class="stage-label" style="left:84px; top:824px;">SEE</span>
  <span class="stage-label" style="left:97px; top:511px;">UNDERSTAND</span>
  <span class="stage-label" style="left:230px; top:370px;">PRIORITISE</span>
  <span class="stage-label" style="left:394px; top:323px;">DESIGN</span>
  <span class="stage-label" style="left:558px; top:370px;">PLAN</span>
  <span class="stage-label" style="left:691px; top:511px;">MOVE</span>
  <span class="stage-label" style="left:704px; top:824px;">LEARN</span>

  <section class="enablers">
    <div class="enabler">
      <div class="enabler-icon"><svg width="44" height="44" viewBox="0 0 44 44"><circle cx="22" cy="22" r="19" fill="var(--icon-ink)"/><path d="M13 22 A9 9 0 1 1 22 31" fill="none" stroke="#fff" stroke-width="3"/><polygon points="22,26 22,36 16,31" fill="#fff"/></svg></div>
      <div class="enabler-name">Adaptive<br>Mindset</div>
    </div>
    <div class="enabler">
      <div class="enabler-icon"><svg width="44" height="44" viewBox="0 0 44 44"><circle cx="22" cy="22" r="19" fill="var(--icon-ink)"/><circle cx="22" cy="14" r="3" fill="none" stroke="#fff" stroke-width="2"/><line x1="22" y1="17" x2="22" y2="32" stroke="#fff" stroke-width="2.5"/><path d="M13 25 Q22 36 31 25" fill="none" stroke="#fff" stroke-width="2.5"/></svg></div>
      <div class="enabler-name">Anchors of<br>Certainty</div>
    </div>
    <div class="enabler">
      <div class="enabler-icon"><svg width="44" height="44" viewBox="0 0 44 44"><polygon points="14,3 30,3 26,18 18,18" fill="var(--icon-ink)"/><circle cx="22" cy="28" r="12" fill="var(--icon-ink)"/><circle cx="22" cy="28" r="6" fill="none" stroke="#fff" stroke-width="2"/></svg></div>
      <div class="enabler-name">The Golden<br>Thread</div>
    </div>
    <div class="enabler">
      <div class="enabler-icon"><svg width="48" height="44" viewBox="0 0 48 44"><g fill="var(--icon-ink)"><circle cx="24" cy="10" r="7"/><rect x="15" y="19" width="18" height="22" rx="5"/><circle cx="9" cy="16" r="5"/><rect x="3" y="23" width="12" height="16" rx="4"/><circle cx="39" cy="16" r="5"/><rect x="33" y="23" width="12" height="16" rx="4"/></g></svg></div>
      <div class="enabler-name">Adaptive<br>Leadership</div>
    </div>
    <div class="enabler">
      <div class="enabler-icon"><svg width="48" height="44" viewBox="0 0 48 44"><g stroke="var(--icon-ink)" stroke-width="2.5" fill="none"><line x1="24" y1="4" x2="24" y2="38"/><line x1="8" y1="10" x2="40" y2="10"/><line x1="14" y1="40" x2="34" y2="40"/></g><g fill="var(--icon-ink)"><path d="M2 24 L8 10 L14 24 Z"/><path d="M34 24 L40 10 L46 24 Z"/></g></svg></div>
      <div class="enabler-name">Balanced<br>Ecosystem</div>
    </div>
    <div class="enabler">
      <div class="enabler-icon"><svg width="44" height="44" viewBox="0 0 44 44"><path d="M8 22 A14 14 0 1 1 22 36" fill="none" stroke="var(--icon-ink)" stroke-width="3.5"/><polygon points="2,20 14,20 8,28" fill="var(--icon-ink)"/><polyline points="22,12 22,22 29,26" fill="none" stroke="var(--icon-ink)" stroke-width="3"/></svg></div>
      <div class="enabler-name">Enduring<br>Commitment</div>
    </div>
  </section>
</div>
</body>
</html>
```